Tallow Inks needs a new Webpage for their collection of ballpens

We at Tallow inks need a brand new webpage to represent our company and range of products. We need a product based website to focus purely on our collection. The web design must bring about a perception of high quality International brand but still affordable in price. Since there are only 5 products, they must all feature on the cover page itself.

Target Market(s)

Stationary Wholesale and retail

Industry/Entity Type

It Company

Number of Pages Required

1 page

Requirements
Must have
• pls see www.quambrite.example to derive inspiration
Should not have
• stock images
• abstract images
• random pen images

```html
<!DOCTYPE html>
<html lang="en">
<head>
<meta charset="utf-8">
<title>Tallow Inks</title>
<link href="https://fonts.googleapis.com/css2?family=Source+Sans+3:wght@400;600;700&family=Varela+Round&display=swap" rel="stylesheet">
<style>
:root{
  --ink:#1c1c1c;
  --white:#ffffff;
  --paper:#fafafa;
  --silver:#b5b5b5;
  --photo-a:#c9d1d3;
  --photo-b:#9ea8ab;
  --faint-a:#eef0ef;
  --faint-b:#d7dbd9;
}
*{margin:0;padding:0;box-sizing:border-box}
html,body{width:1200px;height:1200px;overflow:hidden;background:var(--paper)}
body{position:relative;font-family:"Source Sans 3",sans-serif;color:var(--ink)}
.nav{position:absolute;left:0;top:0;width:1200px;height:80px;background:var(--white);display:flex;justify-content:center;align-items:center;gap:40px}
.nav a{font-family:"Source Sans 3",sans-serif;font-weight:700;font-size:27px;color:var(--ink);text-decoration:none;letter-spacing:.5px}
.hero{position:absolute;left:0;top:80px;width:1200px;height:640px;background:var(--ink)}
.brand{position:absolute;left:0;width:1200px;top:18px;text-align:center;color:var(--white);font-family:"Source Sans 3",sans-serif;font-weight:600;font-size:42px;letter-spacing:8px}
.hero-photo{position:absolute;left:59px;top:150px;width:592px;height:394px;background:linear-gradient(135deg,var(--photo-a),var(--photo-b))}
.hero-copy{position:absolute;left:687px;top:188px;width:450px;height:234px;border:2px solid var(--white);padding:28px 20px 0 37px;color:var(--white);font-size:29.5px;line-height:35px}
.product-tag{position:absolute;left:322px;top:504px;width:556px;height:88px;background:var(--silver);border:2px solid var(--white);display:flex;align-items:center;justify-content:center}
.product-tag span{font-family:"Source Sans 3",sans-serif;font-weight:700;font-size:52px;font-variant:small-caps;color:var(--ink);letter-spacing:1px;margin-top:-2px}
.product-tag svg{position:absolute;top:4px}
.dots{position:absolute;left:1036px;top:580px;display:flex;gap:17px}
.dots i{width:13px;height:13px;border-radius:50%;border:1.5px solid var(--white)}
.dots i.on{background:var(--white)}
.about-photo{position:absolute;left:698px;top:720px;width:502px;height:480px;background:linear-gradient(160deg,var(--faint-a),var(--faint-b))}
.tagline{position:absolute;left:0;width:734px;top:776px;text-align:center;font-family:"Varela Round",sans-serif;font-size:32px;letter-spacing:.5px}
.feature{position:absolute;left:64px;top:879px;width:610px;height:149px;background:var(--ink)}
.icon-tile{position:absolute;width:80px;height:80px;display:flex;align-items:center;justify-content:center}
.feature .icon-tile{left:54px;top:16px;background:var(--white)}
.feature-title{position:absolute;left:23px;top:98px;color:var(--white);font-family:"Varela Round",sans-serif;font-size:34px}
.blurb{position:absolute;font-family:"Varela Round",sans-serif;font-size:22px;line-height:29px;padding:12px 7px 0 7px}
.feature .blurb{left:258px;top:16px;width:329px;height:117px;border:1px solid var(--white);color:var(--white)}
.award{position:absolute;left:62px;top:1082px;width:614px;height:140px;border:2px solid var(--ink);background:var(--white)}
.award .blurb{left:23px;top:17px;width:329px;height:130px;border:1px solid var(--ink);color:var(--ink)}
.award .icon-tile{left:483px;top:17px;background:var(--ink)}
.award-title{position:absolute;left:468px;top:101px;font-family:"Varela Round",sans-serif;font-size:34px}
.about-heading{position:absolute;left:778px;top:1040px;font-family:"Source Sans 3",sans-serif;font-weight:700;font-size:76px;font-variant:small-caps;line-height:1}
.about-brand{position:absolute;left:870px;top:1122px;font-family:"Source Sans 3",sans-serif;font-weight:600;font-size:36px;letter-spacing:6px}
.about-rule{position:absolute;left:775px;top:1182px;width:351px;height:2px;background:var(--ink)}
</style>
</head>
<body>
<nav class="nav"><a href="#">HOME</a><a href="#">ABOUT US</a><a href="#">OUR PRODUCTS</a><a href="#">CONTACT US</a></nav>

<section class="hero">
  <div class="brand">TALLOW INKS</div>
  <div class="hero-photo" role="img" aria-label="Photo of a smiling businesswoman at a desk holding out a ballpen"></div>
  <div class="hero-copy">Lorem ipsum dolor sit amet, consectetur adipiscing elit. Pellentesque venenatis massa tortor, vel blandit erat pulvinar sed.</div>
  <div class="product-tag">
    <svg style="left:6px" width="22" height="80" viewBox="0 0 22 80"><polyline points="20,2 2,40 20,78" fill="none" stroke="#1c1c1c" stroke-width="1"/></svg>
    <span>Modern Pen</span>
    <svg style="right:6px" width="22" height="80" viewBox="0 0 22 80"><polyline points="2,2 20,40 2,78" fill="none" stroke="#1c1c1c" stroke-width="1"/></svg>
  </div>
  <div class="dots"><i class="on"></i><i></i><i></i><i></i></div>
</section>

<div class="about-photo" role="img" aria-label="Faint photo of business people talking in a bright office"></div>

<h2 class="tagline">Global leader in stationery production</h2>

<section class="feature">
  <div class="icon-tile">
    <svg width="64" height="64" viewBox="0 0 64 64"><line x1="6" y1="60" x2="44" y2="22" stroke="#1c1c1c" stroke-width="2.5"/><polygon points="50,6 53,15 62,16 55,22 57,31 50,26 42,30 45,21 38,15 47,15" fill="none" stroke="#1c1c1c" stroke-width="2"/></svg>
  </div>
  <div class="feature-title">Features</div>
  <p class="blurb">Lorem ipsum dolor sit amet, consectetur adipiscing elit. In sed mattis lorem.</p>
</section>

<section class="award">
  <p class="blurb">Lorem ipsum dolor sit amet, consectetur adipiscing elit. In sed mattis lorem.</p>
  <div class="icon-tile">
    <svg width="50" height="60" viewBox="0 0 50 60"><path d="M12 4h26v14c0 9-6 15-13 15S12 27 12 18z" fill="#fff"/><path d="M12 8H4c0 10 5 15 10 15M38 8h8c0 10-5 15-10 15" fill="none" stroke="#fff" stroke-width="3"/><rect x="22" y="32" width="6" height="12" fill="#fff"/><rect x="14" y="44" width="22" height="10" fill="#fff"/></svg>
  </div>
  <div class="award-title">Awards</div>
</section>

<h2 class="about-heading">About</h2>
<div class="about-brand">TALLOW INKS</div>
<div class="about-rule"></div>
</body>
</html>
```